Modern Yoga Studio Timetable and Flyer Design

We have a comprehensive class timetable and we are wanting to a clean modern look for our Spring timetable.

We require a double sided flyer with our class timetable included.
We would prefer an A5 size (postcard) or DL (1/3 A4).

We would like the final flyer to have.
Side A : Yoga image, logo

Fennel Stretch Hall
address: 4/71 Wexcombe Lane, Pelharton
website: fennelstretch.com.au
mobile: 0471 296 814

Side B: Clear easy to read timetable with a break down of class types and website.

We would also like to have a copy of the timetable itself as a separate jpg or pdf for use on our website to download.

Thank you.
Yours kindly,
Nell

I have attached a sample of another timetable of which I like the look and feel of, however this is just a guide. I've also attached our 'new' schedule in WORD plus uploaded our last design of the front.
Updates

Target Market(s)

Women aged 30-45

Industry/Entity Type

Health And Wellness

Font styles to use
Other font styles liked:
• Brandon Grotesque, Jenna Sue

Colors
6c459b
33a6d7
ffffff

Requirements
Must have
• A definitive colour to decipher between different class types on our timetable. Where each colour represents a different class type. Colours and layouts similar to our website design, see www.fennelstretch.com.au
Nice to have
• I've included a design of another studio whose timetable design I like. One of our own yoga images instead of a stock image.
Should not have
• No dark gridlines between the cells/boxes in the timetables. Please don't use stock yoga images.

```html
<!DOCTYPE html>
<html lang="en">
<head>
<meta charset="utf-8">
<title>Fennel Stretch Hall – Spring Flyer</title>
<link rel="stylesheet" href="https://fonts.googleapis.com/css2?family=Josefin+Sans:wght@400;600&display=swap">
<style>
:root{
  --purple:#6c459b;
  --blue:#33a6d7;
  --white:#ffffff;
  --page:#ececec;
  --ink:#4a4a4c;
  --head-grey:#a7a9ac;
  --yellow:#f8e27c;
  --salmon:#ef9d86;
  --mint:#cce8c8;
  --sky:#a8d8e6;
  --slate:#6d6e70;
  --mist:#e4e4e5;
  --tan:#a88f72;
  --rose:#d9aac8;
  --magenta:#cf4f9b;
  --teal:#2f9f8e;
  --lilac:#e7e0f0;
}
*{box-sizing:border-box;margin:0;padding:0}
html,body{width:1200px;height:1000px;overflow:hidden}
body{background:var(--page);font-family:"Josefin Sans",sans-serif;position:relative}

/* Side A */
.flyer-front{position:absolute;left:284px;top:25px;width:632px;height:445px;background:var(--white);overflow:hidden}
.front-ornament{position:absolute;left:236px;top:-60px;width:160px;height:160px;border-radius:50%;background:var(--lilac);opacity:.6}
.brand-name{position:absolute;left:0;right:0;text-align:center;color:var(--blue);font-weight:400;letter-spacing:.18em;text-transform:lowercase;white-space:nowrap}
.flyer-front .brand-name{top:24px;font-size:24px}
.hero-photo{position:absolute;left:0;top:78px;width:632px;height:332px;background:linear-gradient(180deg,#ffffff 0%,#f4f0f4 45%,#e9dfe6 70%,#b28e62 82%,#a3804f 100%)}
.contact-list{position:absolute;right:13px;top:97px;display:flex;flex-direction:column;align-items:flex-end;gap:10px;list-style:none}
.contact-item{position:relative;display:flex;align-items:center;height:28px}
.contact-item .label{background:var(--blue);color:var(--white);font-size:10px;font-weight:600;letter-spacing:.02em;text-transform:uppercase;padding:4px 12px 2px 22px;margin-left:-12px;border-radius:0 10px 10px 0;height:20px;display:flex;align-items:center;white-space:nowrap}
.contact-item .icon{position:relative;z-index:1;width:28px;height:28px;border-radius:50%;background:var(--purple);display:flex;align-items:center;justify-content:center}
.photo-circle{position:absolute;width:128px;height:128px;border-radius:50%;border:4px solid var(--blue);box-shadow:0 0 0 3px var(--white)}
.circle-class{left:19px;top:208px;background:linear-gradient(135deg,#d9c3b0,#7e6a64)}
.circle-pregnancy{left:140px;top:255px;background:linear-gradient(160deg,#f6f6f6,#cfc9c6)}
.circle-kids{left:268px;top:283px;background:linear-gradient(135deg,#b6948a,#5f4e57)}
.tagline{position:absolute;left:0;right:0;top:429px;text-align:center;color:var(--purple);font-size:11.5px;line-height:1;font-weight:600;letter-spacing:.12em;text-transform:uppercase;white-space:nowrap}

/* Side B */
.flyer-back{position:absolute;left:284px;top:490px;width:632px;height:445px;background:var(--blue)}
.flyer-back .brand-name{left:190px;right:auto;top:18px;font-size:20px;color:var(--white);width:250px}
.header-divider{position:absolute;left:449px;top:7px;width:1px;height:44px;background:var(--white)}
.timetable-title{position:absolute;left:464px;top:35px;color:var(--white);font-size:14px;line-height:1;letter-spacing:.03em;text-transform:uppercase;white-space:nowrap}
.timetable-panel{position:absolute;left:6px;top:53px;right:6px;bottom:7px;background:var(--white);border-radius:14px;overflow:hidden}
.panel-ornament{position:absolute;left:170px;top:60px;width:280px;height:280px;border-radius:50%;background:var(--lilac);opacity:.5}
.timetable{position:absolute;left:0;top:7px;display:grid;grid-template-columns:80px repeat(7,71px);grid-template-rows:24px 3px repeat(13,26.3px);column-gap:3px}
.day{grid-row:1;background:var(--head-grey);color:var(--white);border-radius:3px;font-size:14px;display:flex;align-items:center;justify-content:center;padding-top:2px}
.time{grid-column:1;color:var(--ink);font-size:13px;font-weight:600;text-align:right;padding-right:7px;align-self:center;padding-top:2px;white-space:nowrap}
.session{align-self:center;height:22px;border-radius:3px;color:var(--white);font-size:10px;line-height:9px;text-transform:uppercase;display:flex;align-items:center;justify-content:center;text-align:center;padding-top:2px;white-space:nowrap}
.session.wide{font-size:10.5px}
.c-mon{grid-column:2}.c-tue{grid-column:3}.c-wed{grid-column:4}.c-thu{grid-column:5}.c-fri{grid-column:6}.c-sat{grid-column:7}.c-sun{grid-column:8}
.r1{grid-row:3}.r2{grid-row:4}.r3{grid-row:5}.r4{grid-row:6}.r5{grid-row:7}.r6{grid-row:8}.r7{grid-row:9}.r8{grid-row:10}.r9{grid-row:11}.r10{grid-row:12}.r11{grid-row:13}.r12{grid-row:14}.r13{grid-row:15}
.rise{background:var(--yellow);color:var(--ink)}
.vinyasa{background:var(--purple)}
.yin{background:var(--rose);color:var(--ink)}
.slow{background:var(--salmon)}
.pregnancy{background:var(--blue)}
.mumbaby{background:var(--mint);color:var(--ink)}
.kids-older{background:var(--sky);color:var(--ink)}
.kids-young{background:var(--slate)}
.teens{background:var(--mist);color:var(--ink)}
.flow-restore{background:var(--tan)}
.yin-restore{background:var(--magenta)}
.wellness{background:var(--teal)}
.booking-note{position:absolute;right:14px;bottom:8px;color:var(--purple);font-size:9px;white-space:nowrap}
</style>
</head>
<body>

<section class="flyer-front" aria-label="Flyer side A">
  <div class="front-ornament" role="img" aria-label="Faint mandala ornament"></div>
  <div class="hero-photo" role="img" aria-label="Yoga teacher in a side-angle pose on a woven floor mat"></div>
  <h1 class="brand-name">Fennel Stretch Hall</h1>
  <ul class="contact-list">
    <li class="contact-item">
      <span class="icon"><svg width="14" height="16" viewBox="0 0 14 16"><path d="M7 0a5.5 5.5 0 0 0-5.5 5.5C1.5 9.6 7 16 7 16s5.5-6.4 5.5-10.5A5.5 5.5 0 0 0 7 0zm0 7.6a2.1 2.1 0 1 1 0-4.2 2.1 2.1 0 0 1 0 4.2z" fill="#fff"/></svg></span>
      <span class="label">4/71 Wexcombe Lane, Pelharton</span>
    </li>
    <li class="contact-item">
      <span class="icon"><svg width="16" height="16" viewBox="0 0 16 16"><circle cx="8" cy="8" r="6.5" fill="none" stroke="#fff" stroke-width="1.4"/><ellipse cx="8" cy="8" rx="2.8" ry="6.5" fill="none" stroke="#fff" stroke-width="1.2"/><path d="M1.5 8h13" stroke="#fff" stroke-width="1.2"/></svg></span>
      <span class="label">fennelstretch.com.au</span>
    </li>
    <li class="contact-item">
      <span class="icon"><svg width="12" height="16" viewBox="0 0 12 16"><rect x="1" y="0.5" width="10" height="15" rx="2" fill="#fff"/><rect x="2.6" y="2.4" width="6.8" height="9.2" fill="#6c459b"/><circle cx="6" cy="13.6" r="0.9" fill="#6c459b"/></svg></span>
      <span class="label">0471 296 814</span>
    </li>
  </ul>
  <div class="photo-circle circle-class" role="img" aria-label="Group class holding warrior pose in the studio"></div>
  <div class="photo-circle circle-pregnancy" role="img" aria-label="Pregnant student in a side stretch"></div>
  <div class="photo-circle circle-kids" role="img" aria-label="Parent and baby yoga class on mats"></div>
  <p class="tagline">Inclusive, inspiring boutique yoga studio classes for all ages &amp; abilities</p>
</section>

<section class="flyer-back" aria-label="Flyer side B">
  <h2 class="brand-name">Fennel Stretch Hall</h2>
  <span class="header-divider"></span>
  <p class="timetable-title">Spring Timetable</p>
  <div class="timetable-panel">
    <div class="panel-ornament" role="img" aria-label="Faint mandala ornament"></div>
    <div class="timetable">
      <span class="day c-mon">MON</span><span class="day c-tue">TUE</span><span class="day c-wed">WED</span><span class="day c-thu">THU</span><span class="day c-fri">FRI</span><span class="day c-sat">SAT</span><span class="day c-sun">SUN</span>

      <span class="time r1">5:45 AM</span>
      <span class="session rise c-tue r1">Rise+Shine*</span>
      <span class="session rise c-thu r1">Rise+Shine*</span>

      <span class="time r2">9:00 AM</span>
      <span class="session vinyasa c-sat r2">Vinyasa<br>Flow</span>

      <span class="time r3">9 : 15 AM</span>
      <span class="session vinyasa c-tue r3">Vinyasa<br>Flow</span>
      <span class="session yin wide c-sun r3">Yin</span>

      <span class="time r4">9:30 AM</span>
      <span class="session slow wide c-mon r4">Slow Flow</span>
      <span class="session vinyasa c-thu r4">Vinyasa<br>Flow</span>

      <span class="time r5">10:30 AM</span>
      <span class="session pregnancy c-sat r5">Pregnancy*</span>

      <span class="time r6">11:00 AM</span>
      <span class="session mumbaby c-tue r6">Mum+Baby*</span>
      <span class="session mumbaby c-thu r6">Mum+Baby*</span>

      <span class="time r7">12:15 AM</span>
      <span class="session pregnancy c-thu r7">Pregnancy*</span>

      <span class="time r8">4:00 PM</span>
      <span class="session kids-older c-wed r8">Kids 8-12*</span>
      <span class="session kids-young c-thu r8">Kids 5-7*</span>
      <span class="session vinyasa c-sat r8">Vinyasa<br>Flow</span>

      <span class="time r9">4:45 PM</span>
      <span class="session teens c-wed r9">Teens 12-16*</span>

      <span class="time r10">5:00PM</span>
      <span class="session teens c-thu r10">Teens 12-16*</span>

      <span class="time r11">6:00 PM</span>
      <span class="session pregnancy c-mon r11">Pregnancy*</span>
      <span class="session vinyasa c-tue r11">Vinyasa<br>Flow</span>
      <span class="session slow wide c-wed r11">Slow Flow</span>
      <span class="session flow-restore c-fri r11">Flow+<br>Restore</span>

      <span class="time r12">6 : 15 PM</span>
      <span class="session pregnancy c-thu r12">Pregnancy*</span>

      <span class="time r13">7:30 PM</span>
      <span class="session vinyasa c-mon r13">Vinyasa<br>Flow</span>
      <span class="session pregnancy c-tue r13">Pregnancy*</span>
      <span class="session yin-restore c-wed r13">Yin+<br>Restore</span>
      <span class="session wellness c-thu r13">Women's<br>Wellness*</span>
    </div>
    <p class="booking-note">*bookings essential</p>
  </div>
</section>

</body>
</html>
```